Landscape design build company door flyer

I would like this flyer to convey a high-level of professionalism for a company that is excellent with communication with their clients as well as a company that does incredible installations

Went on vacation/holiday

```html
<!DOCTYPE html>
<html lang="en">
<head>
<meta charset="utf-8">
<title>Summit Stone Builders – Door Flyer</title>
<link href="https://fonts.googleapis.com/css2?family=Rubik:wght@400;500;700;800&family=Yellowtail&display=swap" rel="stylesheet">
<style>
:root{
  --stage:#c9c9c9;
  --navy:#173446;
  --navy-deep:#0f2634;
  --teal:#1d4650;
  --grass:#2f4f2a;
  --gold:#f4b223;
  --orange:#f08a1c;
  --paper:#ffffff;
  --map:#eef0f1;
}
*{box-sizing:border-box;margin:0;padding:0}
html,body{width:1200px;height:3226px;overflow:hidden}
body{background:var(--stage);font-family:"Rubik",Arial,sans-serif;position:relative}
p,span,h1,h2{white-space:nowrap}

.flyer{position:absolute;left:100px;width:1000px;height:772px;background:var(--paper);overflow:hidden;box-shadow:0 6px 24px rgba(0,0,0,.18)}
.flyer--front{top:781px}
.flyer--back{top:1673px}

/* ---------- FRONT ---------- */
.hero{position:absolute;left:0;top:0;width:1000px;height:440px;
  background:linear-gradient(180deg,var(--navy-deep) 0%,var(--teal) 62%,var(--grass) 100%)}
.hero-photo{position:absolute;left:0;top:0;width:580px;height:440px;
  background:linear-gradient(160deg,#8a5f36 0%,#5a5048 30%,#6f7478 55%,#3d4a50 100%)}
.headline{position:absolute;left:605px;top:58px;width:370px;font-weight:inherit}
.headline .script{font-family:"Yellowtail",cursive;color:#fff;font-size:66px;line-height:66px;height:66px;display:block;margin-left:28px;font-weight:400}
.headline .big{font-family:"Rubik",sans-serif;font-weight:800;color:var(--gold);font-size:94px;line-height:86px;display:block}
.headline .sub{display:block;color:#fff;font-weight:500;font-size:24px;line-height:28px;margin-top:14px}

.snap{position:absolute;background:#fff;padding:7px;box-shadow:0 4px 10px rgba(0,0,0,.25)}
.snap > div{width:100%;height:100%}
.snap--pool{left:40px;top:404px;width:304px;height:172px;transform:rotate(2deg)}
.snap--pool > div{background:linear-gradient(180deg,#cfd9de 0%,#5e7d4f 40%,#2aa3c6 70%,#d9dcdc 100%)}
.snap--drive{left:338px;top:386px;width:306px;height:182px;transform:rotate(-3deg)}
.snap--drive > div{background:linear-gradient(120deg,#6b6e6e 0%,#8d8f90 40%,#6d5536 60%,#4f5b3a 100%)}

.badge{position:absolute;left:276px;top:380px;width:104px;height:104px;border-radius:50%;
  background:radial-gradient(circle,#f8a23a 0%,var(--orange) 70%);border:4px solid #f9c269;
  color:#fff;text-align:center;font-weight:700}
.badge .get{display:block;font-size:15px;font-weight:500;margin-top:10px}
.badge .pct{display:block;font-size:38px;line-height:1}
.badge .pct small{font-size:14px}
.badge .note{display:block;font-size:9px;font-weight:500}

.brand{position:absolute;left:40px;top:612px;width:260px;text-align:center}
.brand-mark{width:44px;height:44px;background:var(--navy);margin:0 auto 10px}
.brand-name{font-weight:700;color:var(--navy);font-size:19px;line-height:1.1}
.brand-name small{display:block;font-size:10px;letter-spacing:.5px;font-weight:500}

.contact{position:absolute;left:326px;top:600px}
.contact .cta{color:var(--gold);font-weight:500;font-size:16px}
.contact .row{display:flex;align-items:center;gap:10px;color:var(--navy)}
.contact .phone{font-weight:700;font-size:28px;margin-top:10px}
.contact .web{font-size:18px;letter-spacing:1px;margin-top:6px}
.ico{width:16px;height:16px;flex:none}
.btn{display:inline-block;border:1.5px solid var(--gold);color:var(--navy);font-weight:700;
  font-size:11px;letter-spacing:1px;padding:6px 16px;margin-top:12px;white-space:nowrap}

.map{position:absolute;left:640px;top:440px;width:360px;height:332px;
  background:linear-gradient(160deg,var(--map) 0%,#e1e5e7 60%,#f3f4f5 100%)}
.map-title{position:absolute;left:680px;top:456px;width:280px;text-align:center;color:var(--navy);font-size:11px;font-weight:500;line-height:1.3}
.map-title .lic{color:var(--gold);font-size:9px;display:block}

/* ---------- BACK ---------- */
.services-hero{position:absolute;left:0;top:0;width:1000px;height:212px;
  background:linear-gradient(180deg,#1c2d33 0%,#22343a 60%,#4a4f44 100%)}
.services-title{position:absolute;top:36px;left:0;width:1000px;text-align:center;
  font-weight:800;font-size:60px;letter-spacing:6px;color:#fff}
.services-title span{color:var(--gold)}
.footer-band{position:absolute;left:0;top:663px;width:1000px;height:109px;background:var(--gold)}
.card{position:absolute;width:283px;height:224px;background:var(--navy);padding:7px 7px 0}
.card .shot{width:100%;height:168px}
.card .label{color:#fff;font-weight:700;font-size:19px;text-align:center;line-height:46px;letter-spacing:.5px}
.c1{left:40px;top:240px}.c2{left:352px;top:240px}.c3{left:666px;top:240px}
.c4{left:40px;top:489px}.c5{left:352px;top:489px}.c6{left:666px;top:489px}
.c1 .shot{background:linear-gradient(180deg,#b9c7cf 0%,#8f8570 45%,#5e5750 100%)}
.c2 .shot{background:linear-gradient(180deg,#d7cbb6 0%,#7a3c22 45%,#a89c8b 100%)}
.c3 .shot{background:linear-gradient(180deg,#e7eaea 0%,#49b7cc 55%,#cfd7d8 100%)}
.c4 .shot{background:linear-gradient(180deg,#5f6265 0%,#3f4245 60%,#2f3133 100%)}
.c5 .shot{background:linear-gradient(180deg,#5b8a45 0%,#b46a3a 55%,#e08a2c 100%)}
.c6 .shot{background:linear-gradient(180deg,#c4b9a6 0%,#8c6a46 55%,#6f5337 100%)}
.footer{position:absolute;left:0;top:726px;width:1000px;height:34px}
.footer > *{position:absolute;top:0;height:34px;display:flex;align-items:center;gap:8px;white-space:nowrap}
.footer .cta{left:44px;color:#fff;font-weight:500;font-size:16px}
.footer .phone{left:196px;color:var(--navy);font-weight:700;font-size:23px}
.footer .web{left:443px;color:#fff;font-size:19px;letter-spacing:1px}
.footer .btn{left:735px;top:6px;height:24px;margin:0;padding:0 14px;border-color:#fff;color:#fff;font-size:10px}
</style>
</head>
<body>

<section class="flyer flyer--front" aria-label="Flyer front">
  <div class="hero">
    <div class="hero-photo" role="img" aria-label="Photo of a covered outdoor pavilion with stone fireplace at dusk"></div>
    <h1 class="headline">
      <span class="script">Let's Create</span>
      <span class="big">DREAM</span>
      <span class="big">YOUR</span>
      <span class="sub">OUTDOOR LIVING SPACES</span>
    </h1>
  </div>

  <div class="snap snap--pool"><div role="img" aria-label="Photo of a backyard swimming pool"></div></div>
  <div class="snap snap--drive"><div role="img" aria-label="Aerial photo of a paver driveway and garden"></div></div>
  <div class="badge"><span class="get">Get</span><span class="pct">10<small>% OFF</small></span><span class="note">OUR PROJECT</span></div>

  <div class="map" role="img" aria-label="Map of the service area with town pins"></div>
  <p class="map-title">YOUR AREAS WE SERVE<br>OUTDOOR LIVING CONTRACTOR<span class="lic">License # SSB0412</span></p>

  <div class="brand">
    <div class="brand-mark"></div>
    <div class="brand-name">SUMMIT STONE BUILDERS<small>OUTDOOR LIVING SPACES</small></div>
  </div>

  <div class="contact">
    <p class="cta">CALL US NOW!</p>
    <p class="row phone">
      <svg class="ico" viewBox="0 0 16 16"><rect width="16" height="16" rx="2" fill="#f4b223"/><path d="M5 3.5l2 2-1 1.2c.6 1.4 1.7 2.5 3.1 3.1l1.2-1 2 2-1.3 1.6C7.8 12.3 3.7 8.2 3.5 5z" fill="#173446"/></svg>
      (555) 014-2276</p>
    <p class="row web">
      <svg class="ico" viewBox="0 0 16 16"><rect width="16" height="16" rx="2" fill="#f4b223"/><circle cx="8" cy="8" r="4.5" fill="none" stroke="#173446" stroke-width="1.2"/><path d="M3.5 8h9M8 3.5c-2 2.5-2 6.5 0 9M8 3.5c2 2.5 2 6.5 0 9" fill="none" stroke="#173446" stroke-width="1"/></svg>
      summitstonebuilders.com</p>
    <span class="btn">GET A FAST FREE ESTIMATE</span>
  </div>
</section>

<section class="flyer flyer--back" aria-label="Flyer back">
  <div class="services-hero" role="img" aria-label="Photo of a stone seat wall and patio at night"></div>
  <h2 class="services-title">OUR <span>SERVICES</span></h2>
  <div class="footer-band"></div>

  <div class="card c1"><div class="shot" role="img" aria-label="Photo of a paver patio with lounge furniture"></div><p class="label">PAVER PATIOS</p></div>
  <div class="card c2"><div class="shot" role="img" aria-label="Photo of a paver driveway before wooden garage doors"></div><p class="label">PAVER DRIVEWAYS</p></div>
  <div class="card c3"><div class="shot" role="img" aria-label="Photo of a modern swimming pool"></div><p class="label">POOLS</p></div>
  <div class="card c4"><div class="shot" role="img" aria-label="Photo of stone block retaining wall steps"></div><p class="label">RETAINING WALLS</p></div>
  <div class="card c5"><div class="shot" role="img" aria-label="Photo of a round firepit on a paver patio"></div><p class="label">FIREPITS &amp; FIREPLACES</p></div>
  <div class="card c6"><div class="shot" role="img" aria-label="Photo of a wooden deck with dining set"></div><p class="label">DECKS &amp; RAILINGS</p></div>

  <div class="footer">
    <span class="cta">CALL US NOW!</span>
    <span class="phone">
      <svg class="ico" viewBox="0 0 16 16"><rect width="16" height="16" rx="2" fill="#173446"/><path d="M5 3.5l2 2-1 1.2c.6 1.4 1.7 2.5 3.1 3.1l1.2-1 2 2-1.3 1.6C7.8 12.3 3.7 8.2 3.5 5z" fill="#f4b223"/></svg>
      (555) 014-2276</span>
    <span class="web">
      <svg class="ico" viewBox="0 0 16 16"><rect width="16" height="16" rx="2" fill="#173446"/><circle cx="8" cy="8" r="4.5" fill="none" stroke="#f4b223" stroke-width="1.2"/><path d="M3.5 8h9M8 3.5c-2 2.5-2 6.5 0 9M8 3.5c2 2.5 2 6.5 0 9" fill="none" stroke="#f4b223" stroke-width="1"/></svg>
      summitstonebuilders.com</span>
    <span class="btn">GET A FAST FREE ESTIMATE</span>
  </div>
</section>

</body>
</html>
```